Pelbrook Business Cards

Create new business cards with the details below.

Aaron Velst
Director

MB: +61 412 563 904
PH: 1300 417 639
Email: aaron.velst@pelbrook.com.au
Address: 27C Marlow Parade, Campbellfield VIC 3061 Australia
Website: www.pelbrook.com.au

Target Market(s)

Other business

Industry/Entity Type

Business

Requirements
Must have
• must be clean looking

```html
<!DOCTYPE html>
<html lang="en">
<head>
<meta charset="utf-8">
<title>Pelbrook Business Cards</title>
<link rel="stylesheet" href="https://fonts.googleapis.com/css2?family=Montserrat:wght@300;400;700;800&display=swap">
<style>
  :root {
    --backdrop: #e4e4e2;
    --card: #f3f3f2;
    --ink: #2e2e2e;
    --ink-soft: #444444;
    --leaf: #8cb32a;
    --shadow: rgba(0, 0, 0, 0.14);
  }
  * { box-sizing: border-box; margin: 0; padding: 0; }
  html, body {
    width: 1200px;
    height: 900px;
    overflow: hidden;
    background: var(--backdrop);
    font-family: "Montserrat", Arial, sans-serif;
    color: var(--ink);
  }
  .sheet {
    position: relative;
    width: 1200px;
    height: 900px;
  }
  .card {
    position: absolute;
    width: 525px;
    height: 300px;
    background: var(--card);
    box-shadow: 0 6px 18px var(--shadow);
  }
  /* Front */
  .card--front { left: 50px; top: 300px; }
  .brand {
    position: absolute;
    left: 70px;
    top: 112px;
    display: flex;
    align-items: center;
    gap: 16px;
  }
  .brand__square {
    width: 52px;
    height: 52px;
    background: var(--leaf);
  }
  .brand__name {
    font-weight: 800;
    font-size: 40px;
    letter-spacing: 0.5px;
    line-height: 1;
    color: var(--ink);
  }
  .brand__tagline {
    margin-top: 6px;
    font-weight: 700;
    font-size: 13.5px;
    letter-spacing: 1.6px;
    color: var(--ink);
  }
  .card--front .website {
    position: absolute;
    right: 44px;
    bottom: 38px;
  }
  /* Back */
  .card--back { right: 50px; top: 300px; }
  .back__mark {
    position: absolute;
    left: 58px;
    top: 116px;
    width: 68px;
    height: 68px;
    background: var(--leaf);
  }
  .person {
    position: absolute;
    left: 170px;
    top: 56px;
    font-weight: 400;
    font-size: 21px;
    color: var(--ink);
  }
  .person__role {
    font-weight: 400;
    font-size: 11.5px;
    letter-spacing: 0.8px;
    color: var(--ink-soft);
  }
  .person__rule {
    position: absolute;
    left: 170px;
    right: 0;
    top: 94px;
    height: 1.5px;
    background: var(--leaf);
  }
  .contact {
    position: absolute;
    left: 170px;
    top: 110px;
    font-size: 12.5px;
    line-height: 17px;
    font-weight: 400;
    color: var(--ink);
  }
  .contact__label {
    color: var(--leaf);
    letter-spacing: 0.6px;
  }
  .contact__group { margin-bottom: 9px; }
  .website {
    font-size: 12.5px;
    font-weight: 400;
    letter-spacing: 0.3px;
    color: var(--ink);
  }
</style>
</head>
<body>
  <main class="sheet">
    <section class="card card--front" aria-label="Business card front">
      <div class="brand">
        <div class="brand__square"></div>
        <div>
          <div class="brand__name">PELBROOK</div>
          <div class="brand__tagline">PLANTATION SHUTTERS</div>
        </div>
      </div>
      <div class="website">www.pelbrook.com.au</div>
    </section>

    <section class="card card--back" aria-label="Business card back">
      <div class="back__mark"></div>
      <div class="person">Aaron Velst <span class="person__role">| DIRECTOR</span></div>
      <div class="person__rule"></div>
      <div class="contact">
        <div class="contact__group">
          <div><span class="contact__label">MOBILE</span> +61 412 563 904</div>
          <div><span class="contact__label">PHONE</span> 1300 417 639</div>
        </div>
        <div class="contact__group">
          <div><span class="contact__label">EMAIL</span> aaron.velst@pelbrook.com.au</div>
        </div>
        <div class="contact__group">
          <div>27C Marlow Parade, Campbellfield</div>
          <div>VIC 3061 Australia</div>
        </div>
        <div class="website">www.pelbrook.com.au</div>
      </div>
    </section>
  </main>
</body>
</html>
```